Security camera surveillance warning Sign

Security Camera Sign 11" x 11" Red, Yellow and Black (White Background)
I would like a line drawing of camera image attached.
Wording: All Suspicious or Criminal Activity Will Be Reported!
WARNING
24 HOUR SURVEILLANCE

Industry/Entity Type

Security

Colors
ec1f27
000000
ffc214

Requirements
Nice to have
• I uploaded a sign and would like the new design look something like that

```html
<!DOCTYPE html>
<html lang="en">
<head>
<meta charset="utf-8">
<title>24 Hour Surveillance Warning Sign</title>
<link rel="stylesheet" href="https://fonts.googleapis.com/css2?family=Roboto+Condensed:wght@700&display=swap">
<style>
  :root {
    --sign-yellow: #ffc214;
    --sign-red: #ec1f27;
    --ring-red: #c1363a;
    --sign-black: #231f20;
    --sign-white: #ffffff;
    --camera-dark: #2a2a2a;
  }
  html, body {
    margin: 0;
    padding: 0;
    width: 1200px;
    height: 1200px;
    overflow: hidden;
    background: var(--sign-yellow);
  }
  .sign {
    display: block;
    width: 1200px;
    height: 1200px;
    font-family: "Roboto Condensed", "Arial Narrow", sans-serif;
    font-weight: 700;
  }
  .sign-face { fill: var(--sign-white); stroke: var(--sign-red); stroke-width: 5; }
  .notice-line { fill: var(--sign-red); font-size: 80px; }
  .watch-ring { fill: none; stroke: var(--ring-red); stroke-width: 41; }
  .camera-art { fill: var(--camera-dark); }
  .warning-plate { fill: var(--sign-yellow); stroke: var(--ring-red); stroke-width: 7; }
  .warning-word { fill: var(--sign-black); font-size: 152px; }
  .surveillance-line { fill: var(--sign-red); font-size: 112px; }
</style>
</head>
<body>
<svg class="sign" viewBox="0 0 1200 1200" xmlns="http://www.w3.org/2000/svg">
  <rect class="sign-face" x="26" y="26" width="1148" height="1148" rx="44"/>

  <text class="notice-line" x="600" y="147" text-anchor="middle" textLength="524" lengthAdjust="spacingAndGlyphs">All Suspicious or</text>
  <text class="notice-line" x="600" y="239" text-anchor="middle" textLength="1067" lengthAdjust="spacingAndGlyphs">Criminal Activity Will Be Reported!</text>

  <circle class="watch-ring" cx="599" cy="599" r="287"/>

  <rect class="camera-art" x="382" y="415" width="463" height="332" rx="18"
        role="img" aria-label="Line drawing of a wall-mounted security camera"/>

  <rect class="warning-plate" x="247" y="811" width="696" height="168" rx="36"/>
  <text class="warning-word" x="596" y="949" text-anchor="middle" textLength="592" lengthAdjust="spacingAndGlyphs">WARNING</text>

  <text class="surveillance-line" x="602" y="1094" text-anchor="middle" textLength="1069" lengthAdjust="spacingAndGlyphs">24 HOUR SURVEILLANCE</text>
</svg>
</body>
</html>
```